Geschäftspapiere für Coaching und Talent Management
Professionell und freundlich
Zielgruppe
Zielgruppe: Führungskräfte
Tätigkeit: Führungskräfte Coaching und Talent Management
Aufgabenstellung
- Der Briefbogen soll klar und smart/elegant wirken
- Das Logo wurde gerade neu erstellt und füge ich bei
- Die weiteren Daten lade ich hoch sobald der Gewinner gewählt ist. Bitte beim Design beachten, dass folg Informationen zusätzlich zum Logo auf das Briefpapier sollen:
Postleitzahl und Stadt
Strasse und Hausnummer
Website und Email Kontakt
Umsatz St.Nr

```html
<!DOCTYPE html>
<html lang="de">
<head>
<meta charset="utf-8">
<title>Briefbogen Miriam Rehberg</title>
<link href="https://fonts.googleapis.com/css2?family=Lato:wght@400;700&family=Arimo:wght@400;700&family=Open+Sans:wght@700&display=swap" rel="stylesheet">
<style>
  :root {
    --backdrop: #4d4d4d;
    --paper: #ffffff;
    --teal: #033f4c;
    --orange: #e73e17;
    --red: #a0141b;
    --grey-text: #666666;
    --dark-text: #444444;
    --fold: #d6d6d6;
    --mark-tint: #eef3f5;
  }
  * { margin: 0; padding: 0; box-sizing: border-box; }
  html, body { width: 1200px; height: 1200px; overflow: hidden; }
  body { background: var(--backdrop); position: relative; font-family: "Arimo", Arial, sans-serif; }

  .sheet {
    position: absolute; top: 243px; width: 505px; height: 713px;
    background: var(--paper);
    box-shadow: 6px 6px 8px rgba(0,0,0,0.45);
    overflow: hidden;
  }
  .sheet--first { left: 84px; }
  .sheet--follow { left: 651px; }

  .brand { position: absolute; left: 50px; top: 30px; display: flex; align-items: center; gap: 8px; }
  .brand__dot { width: 14px; height: 14px; border-radius: 50%; background: var(--teal); }
  .brand__name { font-family: "Lato", sans-serif; font-weight: 400; font-size: 14.5px; color: var(--teal); letter-spacing: 0.6px; line-height: 1; }

  .sender-line { position: absolute; left: 88px; top: 104px; display: flex; align-items: center; gap: 3px; font-family: "Open Sans", sans-serif; font-weight: 700; font-size: 4.6px; color: #222; }
  .sender-line__dot { width: 6px; height: 6px; border-radius: 50%; background: var(--teal); }
  .sender-line__text { border-bottom: 0.6px solid #bbb; padding-bottom: 1px; }
  .sender-line__sep { color: var(--orange); }

  .contact { position: absolute; left: 358px; top: 22px; border-left: 0.7px solid #aaa; padding-left: 6px; height: 128px; font-size: 6px; line-height: 8.3px; color: var(--grey-text); }
  .contact__label { color: var(--red); display: inline-block; width: 27px; }
  .contact__head { font-weight: 700; color: var(--dark-text); margin-top: 5px; }
  .contact p { white-space: nowrap; }
  .contact__row { margin-top: 3px; }

  .fold { position: absolute; left: 0; width: 18px; height: 0.6px; background: var(--fold); }
  .fold--upper { top: 253px; }
  .fold--lower { top: 492px; }

  .backmark { position: absolute; left: 117px; top: 290px; width: 140px; height: 140px; border-radius: 50%; background: var(--mark-tint); }

  .follow-name { position: absolute; right: 30px; top: 32px; font-family: "Lato", sans-serif; font-weight: 400; font-size: 12px; color: var(--teal); letter-spacing: 0.6px; }

  .footer { position: absolute; left: 0; bottom: 0; width: 505px; height: 32px; }
  .footer__url { position: absolute; right: 17px; bottom: 11px; font-size: 8px; color: #fff; letter-spacing: 0.1px; }
</style>
</head>
<body>

<section class="sheet sheet--first">
  <div class="brand">
    <span class="brand__dot"></span>
    <span class="brand__name">MIRIAM REHBERG</span>
  </div>

  <div class="sender-line">
    <span class="sender-line__dot"></span>
    <span class="sender-line__text">Lindenweg 17 <span class="sender-line__sep">•</span> 30159 Hannover</span>
  </div>

  <div class="contact">
    <p>Am Hang 2</p>
    <p>36100 Talheim am Bach</p>
    <p class="contact__row"><span class="contact__label">Telefon.:</span>+49 0000 41725 - 0</p>
    <p class="contact__row"><span class="contact__label">Fax.:</span>+49 0000 41725-29</p>
    <p class="contact__row"><span class="contact__label">E-Mail.:</span>info@rehberg-post.de</p>
    <p class="contact__head">Bankverbindung:</p>
    <p>Musterbank Nord-Talheim eG</p>
    <p>IBAN: DE 00 1234 5678 9012 3456 78</p>
    <p>BIC: MUSTDEXXTAL</p>
    <p class="contact__head">Handelsregister:</p>
    <p>Amtsgericht Talheim</p>
    <p>HRA 00000</p>
    <p>USt-IdNr: DE00 00000 0</p>
  </div>

  <span class="fold fold--upper"></span>
  <span class="fold fold--lower"></span>
  <div class="backmark" role="img" aria-label="Dezentes Markenzeichen im Hintergrund"></div>

  <svg class="footer" viewBox="0 0 505 32" aria-hidden="true">
    <rect x="1" y="0" width="346" height="1.3" fill="var(--red)"/>
    <rect x="1" y="5.6" width="335" height="1.3" fill="var(--teal)"/>
    <polygon points="0,10.5 330,10.5 309,32 0,32" fill="var(--orange)"/>
    <polygon points="354,0 505,0 505,32 323,32" fill="var(--teal)"/>
  </svg>
  <span class="footer__url">www.neu-medien-beispiel.de</span>
</section>

<section class="sheet sheet--follow">
  <span class="follow-name">MIRIAM REHBERG</span>
  <span class="fold fold--upper"></span>
  <span class="fold fold--lower"></span>
  <div class="backmark" role="img" aria-label="Dezentes Markenzeichen im Hintergrund"></div>

  <svg class="footer" viewBox="0 0 505 32" aria-hidden="true">
    <rect x="1" y="0" width="346" height="1.3" fill="var(--red)"/>
    <rect x="1" y="5.6" width="335" height="1.3" fill="var(--teal)"/>
    <polygon points="0,10.5 330,10.5 309,32 0,32" fill="var(--orange)"/>
    <polygon points="354,0 505,0 505,32 323,32" fill="var(--teal)"/>
  </svg>
  <span class="footer__url">www.neu-medien-beispiel.de</span>
</section>

</body>
</html>
```